Empresa de tecnología busca diseño de tarjetas de presentación

Se requiere tarjeta de presentación impresa, con los datos de contacto y logo de la empresa. (se adjunta una imagen como referencia, esto no significa que deberá de ser igual)

```html
<!DOCTYPE html>
<html lang="en">
<head>
<meta charset="utf-8">
<title>Tremivo IT – Business Cards</title>
<link rel="stylesheet" href="https://fonts.googleapis.com/css2?family=Mulish:wght@300;400;700&display=swap">
<style>
  :root {
    --paper: #efeeea;
    --navy: #183d6e;
    --green: #77bc43;
    --grey-text: #3a3a3a;
    --white: #ffffff;
    --page: #ffffff;
  }
  html, body {
    margin: 0;
    padding: 0;
    width: 900px;
    height: 1200px;
    overflow: hidden;
    background: var(--page);
    font-family: "Mulish", "Helvetica Neue", Arial, sans-serif;
  }
  .canvas {
    position: relative;
    width: 900px;
    height: 1200px;
  }
  .card {
    position: absolute;
    left: 79px;
    width: 775px;
    height: 442px;
    background: var(--paper);
    overflow: hidden;
  }
  .card--front { top: 136px; }
  .card--back { top: 651px; left: 78px; }

  .wordmark {
    position: absolute;
    margin: 0;
    color: var(--navy);
    font-weight: 700;
    white-space: nowrap;
    display: flex;
    align-items: center;
  }
  .wordmark__dot {
    display: inline-block;
    border-radius: 50%;
    background: var(--green);
  }
  .card--front .wordmark {
    left: 62px;
    top: 62px;
    font-size: 40px;
    letter-spacing: 4px;
  }
  .card--front .wordmark__dot { width: 9px; height: 9px; margin-left: 2px; margin-top: 18px; }

  .holder {
    position: absolute;
    right: 35px;
    top: 60px;
    text-align: right;
  }
  .holder__name {
    margin: 0;
    font-size: 30px;
    font-weight: 400;
    color: var(--navy);
    line-height: 1.1;
  }
  .holder__title {
    margin: 3px 0 0;
    font-size: 18px;
    font-weight: 400;
    color: var(--grey-text);
  }

  .contact-panel {
    position: absolute;
    left: 0;
    top: 237px;
    width: 775px;
    height: 205px;
  }
  .contact-panel > svg { position: absolute; left: 0; top: 0; }
  .helpline {
    position: absolute;
    left: 0;
    top: 0;
    width: 775px;
    height: 50px;
    line-height: 42px;
    text-align: center;
    color: var(--white);
    font-size: 22px;
    font-weight: 400;
    margin: 0;
  }
  .contact-list {
    position: absolute;
    left: 48px;
    top: 93px;
    margin: 0;
    padding: 0;
    list-style: none;
    color: var(--white);
    font-size: 17px;
    font-weight: 300;
    line-height: 22px;
  }
  .contact-list li { display: flex; align-items: center; gap: 10px; color: var(--white); }
  .contact-list a { color: var(--white); text-decoration: none; }
  .address {
    position: absolute;
    right: 35px;
    top: 115px;
    margin: 0;
    text-align: right;
    color: var(--white);
    font-size: 17px;
    font-weight: 300;
    line-height: 22px;
    font-style: normal;
  }

  .card--back .wordmark {
    left: 0;
    width: 775px;
    justify-content: center;
    top: 160px;
    font-size: 76px;
    letter-spacing: 11px;
  }
  .card--back .wordmark__dot { width: 14px; height: 14px; margin-top: 38px; }
  .site-link {
    position: absolute;
    left: 0;
    width: 775px;
    top: 396px;
    margin: 0;
    text-align: center;
    font-size: 17px;
    letter-spacing: 3.5px;
    color: var(--grey-text);
  }
  .site-link__accent { color: var(--green); }
</style>
</head>
<body>
<main class="canvas">

  <section class="card card--front" aria-label="Business card front">
    <p class="wordmark">Tremivo IT<span class="wordmark__dot"></span></p>

    <div class="holder">
      <h1 class="holder__name">Lucía Morales</h1>
      <p class="holder__title">Digital Marketing Manager</p>
    </div>

    <div class="contact-panel">
      <svg width="775" height="205" viewBox="0 0 775 205" aria-hidden="true">
        <rect x="0" y="0" width="775" height="205" fill="var(--navy)"/>
        <rect x="0" y="0" width="775" height="50" fill="var(--green)"/>
        <path d="M0 0 A35 50 0 0 1 35 50 L0 50 Z" fill="var(--navy)"/>
        <path d="M775 0 A35 50 0 0 0 740 50 L775 50 Z" fill="var(--navy)"/>
      </svg>
      <p class="helpline">Do you need to lift a ticket? 01 800 3106258</p>

      <ul class="contact-list">
        <li>
          <svg width="11" height="11" viewBox="0 0 24 24" aria-hidden="true"><path fill="var(--white)" d="M6.6 10.8a15.1 15.1 0 0 0 6.6 6.6l2.2-2.2c.3-.3.7-.4 1-.2 1.1.4 2.3.6 3.6.6.6 0 1 .4 1 1V20c0 .6-.4 1-1 1A17 17 0 0 1 3 4c0-.6.4-1 1-1h3.5c.6 0 1 .4 1 1 0 1.3.2 2.5.6 3.6.1.3 0 .7-.2 1z"/></svg>
          <span>(55) 4872 6150 ext. 1 24</span>
        </li>
        <li>
          <svg width="11" height="11" viewBox="0 0 24 24" aria-hidden="true"><path fill="var(--white)" d="M2 8c3-4 17-4 20 0l-1 3h-4l-1-2H8L7 11H3zM5 13h14l2 8H3z"/></svg>
          <span>56 2047 8391</span>
        </li>
        <li>
          <svg width="11" height="11" viewBox="0 0 24 24" aria-hidden="true"><path fill="var(--white)" d="M2 5h20v14H2z"/><path fill="none" stroke="var(--navy)" stroke-width="2" d="M3 6l9 7 9-7"/></svg>
          <a href="mailto:lu.morales@tremivoit.com">lu.morales@tremivoit.com</a>
        </li>
      </ul>

      <address class="address">12th floor, Alvera<br>Tower CDMX</address>
    </div>
  </section>

  <section class="card card--back" aria-label="Business card back">
    <p class="wordmark">Tremivo IT<span class="wordmark__dot"></span></p>
    <p class="site-link">www.<span class="site-link__accent">support@tremivoit</span>.com</p>
  </section>

</main>
</body>
</html>
```